Property Investment eBook Cover

I am a long established Australian property investment adviser, analyst and consultant who is now in semi-retired mode and have re-branded to reflect a more casual and personal approach to advising my property investor clients. I am writing a 'revised edition' to a book written in partnership with my father 20 years ago and need an eBook Cover for this new edition. The eBook will be uploaded to all the regular Australian providers (Larkfield Reader, Quince Folio, Tavi, Pagemarten)

The 3 key elements in the book cover are:

Title: The Harvest Engine of Land. The word 'Property' should be larger and more prominent. eg "The Wealth Power of" could be 1/3 the size of "Property" - with both justified left

Edition: Sydney 2021. "Sydney 2021" should be the focus and dominant imagery of the eBook cover and more prominent than the Title or Author

Author: Colin Marsh, The Housing Ledger Guide. The word "Author" should not appear. "The Housing Ledger Guide" should appear underneath Colin Marsh and justified to Colin Marsh, therefore a smaller font.

The cover should be simple, but eye-catching. No property images, more of an abstract background, than a background with an image. Our preferred colour palette is more blues/greens. Prefer SerifFonts

Copy of book published 20 years ago attached for reference only

```html
<!DOCTYPE html>
<html lang="en">
<head>
<meta charset="utf-8">
<title>The Harvest Engine of Land — Sydney 2021</title>
<link rel="stylesheet" href="https://fonts.googleapis.com/css2?family=Bodoni+Moda:opsz,wght@6..96,400;6..96,500&family=Cormorant+Garamond:wght@500&display=swap">
<style>
  :root {
    --ink: #0d0d0d;
    --aqua-light: #cfe9ec;
    --aqua-mid: #9fd3da;
    --aqua-deep: #6fbfca;
    --gold-dust: #e4d3bf;
    --band: #ffffff;
    --band-rule: #2a2a2a;
  }
  * { margin: 0; padding: 0; box-sizing: border-box; }
  html, body { width: 750px; height: 1200px; overflow: hidden; background: var(--aqua-light); }
  .cover { position: relative; width: 750px; height: 1200px; overflow: hidden; color: var(--ink); }

  .marble {
    position: absolute; left: 0; right: 0;
    background:
      radial-gradient(ellipse at 80% 20%, rgba(228,211,191,0.55), transparent 45%),
      radial-gradient(ellipse at 20% 70%, rgba(111,191,202,0.55), transparent 55%),
      linear-gradient(160deg, var(--aqua-light) 0%, var(--aqua-mid) 55%, var(--aqua-deep) 100%);
  }
  .marble--upper { top: 0; height: 628px; }
  .marble--lower { top: 783px; bottom: 0; }

  .edition-band {
    position: absolute; top: 628px; left: 0; right: 0; height: 155px;
    background: var(--band);
    border-top: 1px solid var(--band-rule);
    border-bottom: 1px solid var(--band-rule);
  }

  .display {
    position: absolute; left: 0; width: 750px; text-align: center;
    font-family: "Bodoni Moda", "Didot", serif;
    font-weight: 400; font-variant: small-caps; line-height: 1;
    white-space: nowrap;
  }
  .title-line { text-shadow: 4px 6px 6px rgba(0,0,0,0.28); padding-left: 30px; }
  .title-the     { top: 92px;  font-size: 70px; }
  .title-middle  { top: 188px; font-size: 86px; }
  .title-of      { top: 310px; font-size: 50px; }
  .title-main    { top: 370px; font-size: 150px; }

  .edition { top: 652px; font-size: 94px; padding-left: 50px; }

  .author-name { top: 996px; font-size: 100px; }
  .author-role {
    position: absolute; left: 0; width: 750px; top: 1095px; text-align: center;
    font-family: "Cormorant Garamond", "Garamond", serif;
    font-weight: 500; font-size: 42px; line-height: 1;
  }
</style>
</head>
<body>
  <main class="cover">
    <div class="marble marble--upper" role="img" aria-label="Abstract aqua alcohol-ink marble with gold veins"></div>
    <div class="edition-band"></div>
    <div class="marble marble--lower" role="img" aria-label="Abstract aqua alcohol-ink marble with gold veins"></div>

    <h1>
      <span class="display title-line title-the">The</span>
      <span class="display title-line title-middle">Harvest Engine</span>
      <span class="display title-line title-of">of</span>
      <span class="display title-line title-main">Land</span>
    </h1>

    <p class="display edition">Sydney 2021</p>

    <p class="display author-name">Colin Marsh</p>
    <p class="author-role">The Housing Ledger Guide.</p>
  </main>
</body>
</html>
```